Looking for a cool, modern Cannabis Jar Label

I want you to come up with a better, modern look for a label.

I need it sized to 4” x 3” - I plan to print directly to label printer.

I want you to use Photoshop and deliver me a layered PSD file that I can edit and modify the information as needed..

The label information will need to include places for:
(1) Strain Name - most important part of label - larger font size than rest - example Kelvin Thistle, TRP #7, Copperleaf Dunes
(2) Pricing - for Gram, 1/8, 1/4, 1/2. and Ounce
(3) Strain Designation (Hybrid, Indica or Sativa) - maybe color coded, different color for Indica v. Sativa, just an idea
(4) THC and CBD percentages - for example 23% THC and 0.05% CBD
(5) Farm name - a place where we can add the name/logo of the business that produced the product. example - Brosk Farms

I have attached a simple mockup showing the information.

I have also attached a few samples of labels we like to give you an idea of the look and feel we are going for.

I am wanting a very clean, modern, classy, readable look.The font will use is Gotham Font.

HI Everyone! Thank you for all of your designs. I am requesting an extension because I need more time to give adequate feedback to the designers. Thank you for your participation and all of your efforts! I will be making a decision soon!

• Gotham Font

• Thank you for your designs. I am sorry i have been slow in providing feedback, things have been really busy around here!
• I wanted to give some group general feedback. After reviewing all of the designs, there is a common theme among all of the designs that I would like to see changed.
• I would like to see the per gram pricing more prominent on the label. This is what most people are looking for when they are purchasing the product. So I would like to see this stand out from the other pricing tiers. As I think about it, they don't all need to be grouped together in a line. You could have the Per Gram pricing front and center some where and then the other pricing tiers grouped together somewhere else on the label.
• This is the order of importance of items on the label. Items at the the top of the list should be bigger than those below it.
• 1. Strain name
• 2. Pricing - being per gram the most important of all prices
• 3. THC/CBD percentages
• 4. Strain Type (indica, sativa, hybrid)
• 5. Farm name/logo
• When laying out these labels, they will be going on rounded jars and they will be on display. Think of jars with fancy labels in a candy store. They need to be eye catchy, appealing, but easy read.
• Thank you for all of your hard work, everyone is doing a great job.
• Best,
• Neta

```html
<!DOCTYPE html>
<html lang="en">
<head>
<meta charset="utf-8">
<title>Copperleaf Dunes – Jar Label</title>
<link rel="stylesheet" href="https://fonts.googleapis.com/css2?family=Montserrat:wght@400;500;700;800&display=swap">
<style>
  :root {
    --page-bg: #e6e7ea;
    --label-bg: #ffffff;
    --ink: #111111;
    --quarter: #7fe6f4;
    --eighth: #3cc6ee;
    --gram: #19b1ae;
    --half: #149fc6;
    --ounce: #0b8dd2;
    --hybrid: #f47a20;
    --thc: #7b7b7b;
    --cbd: #b7b7b7;
  }
  * { box-sizing: border-box; margin: 0; padding: 0; }
  html, body {
    width: 1200px;
    height: 840px;
    overflow: hidden;
    background: var(--page-bg);
    font-family: "Montserrat", sans-serif;
    color: var(--ink);
  }
  .label {
    position: absolute;
    left: 80px;
    top: 60px;
    width: 1040px;
    height: 720px;
    background: var(--label-bg);
  }
  .strain-name {
    position: absolute;
    left: 0;
    right: 0;
    top: 66px;
    text-align: center;
    font-size: 66px;
    font-weight: 800;
    letter-spacing: 1px;
    line-height: 1;
    padding-left: 70px;
  }
  .rule-h {
    position: absolute;
    left: 60px;
    right: 60px;
    height: 0;
    border-top: 7px dotted var(--ink);
  }
  .rule-h.top { top: 166px; }
  .rule-h.mid { top: 408px; }
  .rule-v {
    position: absolute;
    left: 550px;
    top: 420px;
    bottom: 18px;
    width: 0;
    border-left: 7px dotted var(--ink);
  }
  .price {
    position: absolute;
    border-radius: 50%;
    display: flex;
    flex-direction: column;
    align-items: center;
    justify-content: center;
    line-height: 1.1;
    transform: translate(-50%, -50%);
  }
  .price .unit { font-size: 30px; font-weight: 400; }
  .price .amount { font-size: 32px; font-weight: 800; }
  .price.quarter { left: 130px; top: 294px; width: 108px; height: 108px; background: var(--quarter); }
  .price.eighth  { left: 313px; top: 294px; width: 108px; height: 108px; background: var(--eighth); }
  .price.gram    { left: 512px; top: 290px; width: 142px; height: 142px; background: var(--gram); }
  .price.gram .unit { font-size: 40px; }
  .price.gram .amount { font-size: 40px; }
  .price.half    { left: 722px; top: 294px; width: 108px; height: 108px; background: var(--half); }
  .price.ounce   { left: 910px; top: 290px; width: 124px; height: 124px; background: var(--ounce); }
  .price.ounce .unit { font-size: 28px; }
  .strain-type {
    position: absolute;
    left: 60px;
    width: 430px;
    top: 456px;
    text-align: center;
    font-size: 62px;
    font-weight: 800;
    color: var(--hybrid);
    line-height: 1;
  }
  .potency {
    position: absolute;
    border-radius: 50%;
    width: 122px;
    height: 122px;
    display: flex;
    flex-direction: column;
    align-items: center;
    justify-content: center;
    line-height: 1.1;
    transform: translate(-50%, -50%);
  }
  .potency .value { font-size: 26px; font-weight: 800; }
  .potency .name { font-size: 26px; font-weight: 400; }
  .potency.thc { left: 206px; top: 619px; background: var(--thc); }
  .potency.cbd { left: 405px; top: 619px; background: var(--cbd); }
  .farm {
    position: absolute;
    left: 557px;
    right: 40px;
    top: 540px;
    display: flex;
    align-items: center;
    justify-content: center;
    gap: 18px;
  }
  .farm-mark {
    width: 62px;
    height: 62px;
    border-radius: 50%;
    border: 4px solid var(--ink);
  }
  .farm-name {
    font-size: 44px;
    font-weight: 800;
    line-height: 1;
    text-transform: uppercase;
  }
</style>
</head>
<body>
  <main class="label">
    <h1 class="strain-name">COPPERLEAF DUNES</h1>
    <div class="rule-h top"></div>

    <div class="price quarter"><span class="unit">1/4</span><span class="amount">00$</span></div>
    <div class="price eighth"><span class="unit">1/8</span><span class="amount">00$</span></div>
    <div class="price gram"><span class="unit">g</span><span class="amount">00$</span></div>
    <div class="price half"><span class="unit">½</span><span class="amount">00$</span></div>
    <div class="price ounce"><span class="unit">Ounce</span><span class="amount">00$</span></div>

    <div class="rule-h mid"></div>
    <div class="rule-v"></div>

    <p class="strain-type">HYBRID</p>
    <div class="potency thc"><span class="value">23%</span><span class="name">THC</span></div>
    <div class="potency cbd"><span class="value">0.05%</span><span class="name">CBD</span></div>

    <div class="farm">
      <span class="farm-mark"></span>
      <span class="farm-name">Brosk Farms</span>
    </div>
  </main>
</body>
</html>
```